Etiketten-Design für Blended Scotch Whisky
Zielgruppe
Internationale Kunden und Importeure sind unsere Kunden, daher suchen wir Internationalität in Punkto Design und Ettiket.
Aufgabenstellung
Wir suchen ein Ettiket für einen Blended Scotch Whisky, wie schon erwähnt sollte es eine internationalen Touch haben.Bitte nur Firmen, die schon diese Art von Etiketten entworfen haben.

```html
<!DOCTYPE html>
<html lang="en">
<head>
<meta charset="utf-8">
<title>Scotch Whisky Label</title>
<link rel="stylesheet" href="https://fonts.googleapis.com/css2?family=Oswald:wght@500;600&family=Graduate&display=swap">
<style>
  :root {
    --backdrop: #f2f2f0;
    --label-black: #000000;
    --gold: #d8b27d;
    --gold-dim: #3a2f20;
    --cream: #f1ece0;
    --teal: #00837c;
    --teal-deep: #005f5a;
    --ink: #0a0a0a;
  }
  html, body {
    margin: 0;
    width: 1200px;
    height: 1200px;
    overflow: hidden;
    background: var(--backdrop);
  }
  .canvas {
    position: relative;
    width: 1200px;
    height: 1200px;
  }
  .label {
    position: absolute;
    left: 151px;
    top: 38px;
    width: 897px;
    height: 1123px;
    display: block;
  }
  .label-ground { fill: var(--label-black); }
  .frame-line { fill: none; stroke: var(--gold); stroke-width: 2; }
  .frame-line--bold { stroke-width: 4; }
  .diamond-band { fill: var(--label-black); stroke: var(--gold); stroke-width: 15; stroke-linejoin: miter; }
  .diamond-rule { fill: none; stroke: var(--gold); stroke-width: 1.5; }
  .side-stripes { fill: var(--gold); opacity: 0.55; }
  .title-scotch {
    font-family: "Oswald", sans-serif;
    font-weight: 600;
    font-size: 80px;
    fill: var(--cream);
    letter-spacing: -1px;
  }
  .title-whisky {
    font-family: "Graduate", serif;
    font-size: 150px;
    fill: var(--cream);
    stroke: var(--gold);
    stroke-width: 1.5;
  }
  .divider { stroke: var(--cream); stroke-width: 2; }
  .divider-tip { fill: var(--cream); }
  .divider-centre { fill: var(--gold); }
  .info-band { fill: var(--teal); }
  .info-band-edge { fill: none; stroke: var(--teal); stroke-width: 6; stroke-dasharray: 4 6; }
  .info-band-inner { fill: none; stroke: var(--ink); stroke-width: 3; }
  .band-dot { fill: var(--ink); }
  .band-text {
    font-family: "Oswald", sans-serif;
    font-weight: 500;
    font-size: 24px;
    fill: var(--ink);
  }
</style>
</head>
<body>
<main class="canvas">
  <svg class="label" viewBox="0 0 897 1123" xmlns="http://www.w3.org/2000/svg">
    <defs>
      <linearGradient id="ornamentTone" x1="0" y1="0" x2="0" y2="1">
        <stop offset="0" stop-color="#4a3b27"/>
        <stop offset="1" stop-color="#2c2418"/>
      </linearGradient>
      <linearGradient id="bandOrnamentTone" x1="0" y1="0" x2="0" y2="1">
        <stop offset="0" stop-color="#004f4b"/>
        <stop offset="1" stop-color="#006b65"/>
      </linearGradient>
    </defs>

    <rect class="label-ground" x="0" y="0" width="897" height="1123"/>

    <g class="info">
      <rect class="info-band" x="113" y="810" width="670" height="245"/>
      <rect class="info-band-edge" x="116" y="813" width="664" height="239"/>
      <rect class="info-band-inner" x="128" y="830" width="640" height="205"/>
      <rect x="329" y="839" width="238" height="173" rx="40"
            fill="url(#bandOrnamentTone)" role="img" aria-label="Symmetrical scroll ornament in dark teal"/>
      <circle class="band-dot" cx="322" cy="1004" r="4"/>
      <circle class="band-dot" cx="574" cy="1004" r="4"/>
      <text class="band-text" x="165" y="970">55,8 % VOL.</text>
      <text class="band-text" x="616" y="970">0,5 L</text>
    </g>

    <g class="frame">
      <rect x="125" y="104" width="646" height="674" fill="url(#ornamentTone)"
            role="img" aria-label="Gold filigree leaf and scroll ornaments in the four corners"/>
      <rect class="frame-line frame-line--bold" x="113" y="92" width="670" height="698"/>
      <rect class="frame-line" x="123" y="102" width="650" height="678"/>
    </g>

    <g class="diamond">
      <polygon class="diamond-band" points="448,60 818,444 448,828 78,444"/>
      <polygon class="diamond-rule" points="448,86 793,444 448,802 103,444"/>
      <path d="M448 108 L550 214 Q448 290 346 214 Z" fill="url(#ornamentTone)"
            role="img" aria-label="Gold filigree ornament at the top of the diamond"/>
      <path d="M340 676 Q448 600 556 676 L448 788 Z" fill="url(#ornamentTone)"
            role="img" aria-label="Gold filigree ornament at the bottom of the diamond"/>
      <polygon class="side-stripes" points="113,385 152,385 152,510 113,510 100,444"
               role="img" aria-label="Fine gold line pattern"/>
      <polygon class="side-stripes" points="745,385 784,385 797,444 784,510 745,510"
               role="img" aria-label="Fine gold line pattern"/>
    </g>

    <g class="title">
      <text class="title-scotch" x="437" y="370" text-anchor="middle">SCOTCH</text>
      <text class="title-whisky" x="452" y="499" text-anchor="middle" textLength="410" lengthAdjust="spacingAndGlyphs">WHISKY</text>
      <line class="divider" x1="282" y1="532" x2="619" y2="532"/>
      <polygon class="divider-tip" points="270,532 282,526 282,538"/>
      <polygon class="divider-tip" points="631,532 619,526 619,538"/>
      <ellipse class="divider-centre" cx="450" cy="532" rx="34" ry="8"
               role="img" aria-label="Small scroll flourish"/>
    </g>
  </svg>
</main>
</body>
</html>
```